Selka Marrow Photography Business Card

I need a new business card/ possibly design to use for other marking materials ... I have included my logo below in a few different colors, but can also provide the logo in additional colors and sizes. I would love a card the expresses clean, simple and classy.

Target Market(s)

Portrait photography clients, child photography clients

Industry/Entity Type

Photographer

Contact Information for Business Card

Selka Marrow Photography, Fenwick MA, www.selkamarrowphotography.example
T. 555-283-9146 E. selkamarrowphoto@mailbox.example

Colors
33b8a4
eea4c8
5c5c5c

Requirements
Must have
• I would like to include my logo on card.
Nice to have
• I also like the color brown as well as the choices below. I would like a simple, elegant card, something classy.

```html
<!DOCTYPE html>
<html lang="en">
<head>
<meta charset="utf-8">
<title>Selka Marrow Photography – Business Card</title>
<link href="https://fonts.googleapis.com/css2?family=Bebas+Neue&display=swap" rel="stylesheet">
<style>
  :root {
    --stage: #5d5c63;
    --card: #242122;
    --frame: #e9e4e6;
    --pink: #eea4c8;
    --white: #f4f1f2;
    --rule: #8c8689;
  }
  html, body {
    margin: 0;
    width: 1200px;
    height: 675px;
    overflow: hidden;
    background: var(--stage);
  }
  .stage {
    position: relative;
    width: 1200px;
    height: 675px;
    display: flex;
    align-items: center;
    justify-content: center;
    gap: 40px;
  }
  .card {
    position: relative;
    width: 540px;
    height: 308px;
    background: var(--card);
    box-shadow: 0 6px 18px rgba(0,0,0,.35);
    font-family: "Bebas Neue", "Arial Narrow", sans-serif;
    overflow: hidden;
  }
  .card__frame {
    position: absolute;
    inset: 16px;
    border: 1.5px solid var(--frame);
  }
  .front__title {
    position: absolute;
    left: 0; right: 0;
    top: 112px;
    text-align: center;
  }
  .front__name {
    color: var(--pink);
    font-size: 34px;
    letter-spacing: 1px;
    line-height: 1;
  }
  .front__rule {
    width: 90px;
    height: 1px;
    background: var(--rule);
    margin: 3px auto 4px;
  }
  .front__sub {
    color: var(--white);
    font-size: 14px;
    letter-spacing: 4px;
    line-height: 1;
  }
  .contact {
    position: absolute;
    left: 26px;
    right: 26px;
    bottom: 30px;
    display: flex;
    align-items: center;
    justify-content: center;
    gap: 7px;
    color: var(--white);
    font-size: 10px;
    letter-spacing: .2px;
    line-height: 1;
  }
  .contact__item {
    display: flex;
    align-items: center;
    gap: 4px;
    white-space: nowrap;
  }
  .contact__sep {
    width: 1px;
    height: 12px;
    background: var(--rule);
    flex: none;
  }
  .contact__icon {
    width: 9px;
    height: 9px;
    flex: none;
  }
  .back__brand {
    position: absolute;
    left: 0; right: 0;
    top: 50%;
    transform: translateY(-50%);
    text-align: center;
    color: var(--pink);
    line-height: 1;
  }
  .back__name {
    font-size: 34px;
    letter-spacing: 2px;
  }
  .back__sub {
    margin-top: 6px;
    font-size: 14px;
    letter-spacing: 4px;
  }
</style>
</head>
<body>
<main class="stage">

  <section class="card card--front" aria-label="Card front">
    <div class="card__frame"></div>
    <div class="front__title">
      <div class="front__name">Selka Marrow</div>
      <div class="front__rule"></div>
      <div class="front__sub">Photography</div>
    </div>
    <div class="contact">
      <span class="contact__item">
        <svg class="contact__icon" viewBox="0 0 12 12"><path d="M6 1a3.5 3.5 0 0 0-3.5 3.5C2.5 7.2 6 11 6 11s3.5-3.8 3.5-6.5A3.5 3.5 0 0 0 6 1z" fill="none" stroke="#eea4c8" stroke-width="1.3"/><circle cx="6" cy="4.5" r="1.2" fill="#eea4c8"/></svg>
        Fenwick MA
      </span>
      <span class="contact__sep"></span>
      <span class="contact__item">
        <svg class="contact__icon" viewBox="0 0 12 12"><path d="M3 1.5l1.6 2.2-1 1.1a6 6 0 0 0 3.6 3.6l1.1-1 2.2 1.6-.9 1.5C5.5 10.5 1.5 6.5 1.5 2.4z" fill="#eea4c8"/></svg>
        555-283-9146
      </span>
      <span class="contact__sep"></span>
      <span class="contact__item">
        <svg class="contact__icon" viewBox="0 0 12 12"><rect x="1" y="2.5" width="10" height="7" fill="#eea4c8"/><path d="M1 2.5l5 4 5-4" fill="none" stroke="#242122" stroke-width="1"/></svg>
        selkamarrowphoto@mailbox.example
      </span>
      <span class="contact__sep"></span>
      <span class="contact__item">
        <svg class="contact__icon" viewBox="0 0 12 12"><circle cx="6" cy="6" r="4.8" fill="none" stroke="#eea4c8" stroke-width="1.2"/><path d="M1.2 6h9.6M6 1.2c-2.4 2.6-2.4 7 0 9.6M6 1.2c2.4 2.6 2.4 7 0 9.6" fill="none" stroke="#eea4c8" stroke-width="1"/></svg>
        www.selkamarrowphotography.example
      </span>
    </div>
  </section>

  <section class="card card--back" aria-label="Card back">
    <div class="card__frame"></div>
    <div class="back__brand">
      <div class="back__name">Selka Marrow</div>
      <div class="back__sub">Photography</div>
    </div>
  </section>

</main>
</body>
</html>
```